Land Buying Company Needs Letterhead for Direct Mail Marketing to Land Owners

We are looking for a professional letterhead that we will be including in our direct mail marketing. We will be sending this to land owners who may be interested in selling or purchasing land.

The letterhead needs to be editable. Headers and footers would look nice, but we are open. We would want it to include our address, website, phone, and email info. For right now the address to use for design purposes would the following:

Address: 415 Bramwell Avenue #600
Dallas, TX 75219
Website - www.quillridgeacres.example
Email - info@quillridgeacres.example
Phone - 866-402-ACRE

I have attached our logo zip file that we just had done on Pixel Guild. Let me know what questions you have, and thank you.

```html
<!DOCTYPE html>
<html lang="en">
<head>
<meta charset="UTF-8">
<title>Quillridge Acres Letterhead</title>
<link href="https://fonts.googleapis.com/css2?family=Montserrat:wght@600&family=Barlow:wght@400&display=swap" rel="stylesheet">
<style>
  :root {
    --forest: #465a1e;
    --leaf: #95c93a;
    --mist: #eaf3da;
    --paper: #ffffff;
  }
  html, body {
    margin: 0;
    padding: 0;
    overflow: hidden;
    background: var(--paper);
  }
  .letterhead {
    position: relative;
    width: 918px;
    height: 1200px;
    background: var(--paper);
    overflow: hidden;
  }
  .masthead {
    position: absolute;
    left: 87px;
    top: 76px;
    width: 733px;
    height: 123px;
    background: var(--forest);
    display: flex;
    align-items: center;
    justify-content: center;
    gap: 18px;
  }
  .masthead-rule {
    position: absolute;
    left: 87px;
    top: 199px;
    width: 733px;
    height: 9px;
    background: var(--leaf);
  }
  .brand-dot {
    width: 78px;
    height: 78px;
    border-radius: 50%;
    background: var(--paper);
    flex: none;
  }
  .brand-name {
    font-family: "Montserrat", sans-serif;
    font-weight: 600;
    font-size: 34px;
    letter-spacing: 1px;
    color: var(--leaf);
    text-transform: uppercase;
    white-space: nowrap;
  }
  .watermark {
    position: absolute;
    left: 335px;
    top: 476px;
    width: 238px;
    height: 238px;
    border-radius: 50%;
    background: var(--mist);
  }
  .contact-band {
    position: absolute;
    left: 87px;
    top: 1054px;
    width: 733px;
    height: 29px;
    background: var(--leaf);
    display: flex;
    align-items: center;
    justify-content: center;
    gap: 6px;
    font-family: "Barlow", sans-serif;
    font-size: 11px;
    color: var(--forest);
    white-space: nowrap;
  }
  .contact-item {
    display: flex;
    align-items: center;
    gap: 3px;
  }
  .contact-icon {
    width: 10px;
    height: 10px;
    flex: none;
  }
  .footer-base {
    position: absolute;
    left: 87px;
    top: 1083px;
    width: 733px;
    height: 27px;
    background: var(--forest);
  }
</style>
</head>
<body>
  <main class="letterhead">
    <header>
      <div class="masthead">
        <span class="brand-dot"></span>
        <span class="brand-name">Quillridge Acres</span>
      </div>
      <div class="masthead-rule"></div>
    </header>

    <div class="watermark" aria-hidden="true"></div>

    <footer>
      <div class="contact-band">
        <span class="contact-item">415 Bramwell Avenue #600, Dallas, TX 75219</span>
        <span class="contact-item">
          <svg class="contact-icon" viewBox="0 0 10 10" aria-hidden="true">
            <circle cx="5" cy="5" r="4.3" fill="none" stroke="#465a1e" stroke-width="0.8"/>
            <ellipse cx="5" cy="5" rx="1.8" ry="4.3" fill="none" stroke="#465a1e" stroke-width="0.6"/>
            <line x1="0.7" y1="5" x2="9.3" y2="5" stroke="#465a1e" stroke-width="0.6"/>
          </svg>
          www.quillridgeacres.example
        </span>
        <span class="contact-item">
          <svg class="contact-icon" viewBox="0 0 10 10" aria-hidden="true">
            <rect x="0.5" y="2" width="9" height="6" fill="#465a1e"/>
            <polyline points="0.5,2 5,5.6 9.5,2" fill="none" stroke="#95c93a" stroke-width="0.7"/>
          </svg>
          info@quillridgeacres.example
        </span>
        <span class="contact-item">
          <svg class="contact-icon" viewBox="0 0 10 10" aria-hidden="true">
            <circle cx="5" cy="5" r="4.4" fill="none" stroke="#465a1e" stroke-width="0.8"/>
            <path d="M3.3 2.8 L4.2 2.6 L4.6 3.9 L4 4.3 Q4.6 5.6 5.8 6.1 L6.2 5.5 L7.4 5.9 L7.2 6.9 Q4.6 7.3 3.1 4.2 Z" fill="#465a1e"/>
          </svg>
          866-402-ACRE
        </span>
      </div>
      <div class="footer-base"></div>
    </footer>
  </main>
</body>
</html>
```